Business Cards for an 'affordable luxury' inner city home builder in Calgary.

We need a business card design that emulates the progressive, innovative, culture of our company and the modern style of our homes. Use our website www.velmarbuilds-ex.com as a reference for the product we build.

Our company builds homes in the inner city space of Calgary, Alberta. We build affordable luxury.

Target Market(s)

Young professional Families

Contact Information for Business Card

Try to maintain consistency with the logo font and the card font.

Requirements
Must have
• The details must include: Name, education, title, phone number, website and email (Address is not as important)
• The design must be uniques (like our logo), elegant, sophisticated and modern.

```html
<!DOCTYPE html>
<html lang="en">
<head>
<meta charset="utf-8">
<title>Velmar Builds — Business Card</title>
<link rel="stylesheet" href="https://fonts.googleapis.com/css2?family=Montserrat:wght@600;700&family=Open+Sans:wght@400&display=swap">
<style>
  :root {
    --page-bg: #e7e5e2;
    --card-black-edge: #2c2c2c;
    --card-black: #1b1b1b;
    --ink: #111111;
    --ink-soft: #8a8a8a;
    --rule: #9a9a9a;
    --band: #242424;
    --silver: #b9b9b9;
    --icon: #7d7d7d;
  }
  * { box-sizing: border-box; margin: 0; padding: 0; }
  html, body { width: 1200px; height: 900px; overflow: hidden; }
  body {
    background: var(--page-bg);
    font-family: "Open Sans", Arial, sans-serif;
    position: relative;
  }
  .card {
    position: absolute;
    left: 250px;
    width: 700px;
    height: 400px;
    overflow: hidden;
    box-shadow: 0 6px 18px rgba(0,0,0,.18);
  }

  /* Back of card */
  .card-back {
    top: 30px;
    background: linear-gradient(160deg, var(--card-black-edge) 0%, var(--card-black) 55%, #141414 100%);
  }
  .card-back .brand {
    position: absolute;
    left: 0; right: 0;
    top: 178px;
    display: flex;
    justify-content: center;
    align-items: center;
    gap: 18px;
  }
  .card-back .brand-square {
    width: 36px; height: 36px;
    background: var(--silver);
  }
  .card-back .brand-name {
    font-family: "Montserrat", Arial, sans-serif;
    font-weight: 600;
    font-size: 30px;
    line-height: 1;
    letter-spacing: 1px;
    color: var(--silver);
  }

  /* Front of card */
  .card-front {
    top: 470px;
    background: linear-gradient(170deg, #ffffff 0%, #f7f7f7 60%, #ffffff 100%);
  }
  .card-front .brand {
    position: absolute;
    right: 50px;
    top: 60px;
    display: flex;
    align-items: center;
    gap: 12px;
  }
  .card-front .brand-square {
    width: 22px; height: 22px;
    background: var(--ink);
  }
  .card-front .brand-name {
    font-family: "Montserrat", Arial, sans-serif;
    font-weight: 600;
    font-size: 22px;
    line-height: 1;
    letter-spacing: 0.5px;
    color: var(--ink);
  }
  .person {
    position: absolute;
    left: 90px;
    top: 115px;
  }
  .person-name {
    font-family: "Montserrat", Arial, sans-serif;
    font-weight: 700;
    font-size: 25px;
    letter-spacing: -0.3px;
    color: var(--ink);
    text-transform: uppercase;
  }
  .person-title {
    font-family: "Montserrat", Arial, sans-serif;
    font-weight: 600;
    font-size: 14px;
    letter-spacing: 1.5px;
    color: var(--ink-soft);
    text-transform: uppercase;
    margin-top: 2px;
  }
  .divider {
    position: absolute;
    left: 80px;
    right: 50px;
    top: 190px;
    height: 1px;
    background: var(--rule);
  }
  .contacts {
    position: absolute;
    left: 80px;
    top: 210px;
    list-style: none;
  }
  .contacts li {
    display: flex;
    align-items: center;
    gap: 12px;
    font-size: 14.5px;
    color: var(--ink);
    height: 29px;
  }
  .contacts svg { width: 14px; height: 14px; flex: none; }
  .address {
    position: absolute;
    right: 50px;
    top: 255px;
    display: flex;
    align-items: flex-start;
    gap: 12px;
    font-size: 14.5px;
    font-style: normal;
    color: var(--ink);
    text-align: right;
    line-height: 1.9;
  }
  .address svg { width: 16px; height: 20px; margin-top: 6px; }
  .footer-band {
    position: absolute;
    left: 0; right: 0; bottom: 0;
    height: 48px;
    background: var(--band);
  }
</style>
</head>
<body>

  <section class="card card-back" aria-label="Card back">
    <div class="brand">
      <span class="brand-square"></span>
      <span class="brand-name">Velmar Builds</span>
    </div>
  </section>

  <section class="card card-front" aria-label="Card front">
    <div class="brand">
      <span class="brand-square"></span>
      <span class="brand-name">Velmar Builds</span>
    </div>

    <div class="person">
      <h1 class="person-name">Your Name</h1>
      <p class="person-title">Job Title</p>
    </div>

    <div class="divider"></div>

    <ul class="contacts">
      <li>
        <svg viewBox="0 0 14 14" aria-hidden="true"><rect x="3.5" y="0.5" width="7" height="13" rx="1.2" fill="none" stroke="var(--icon)" stroke-width="1.2"/><line x1="6" y1="11.3" x2="8" y2="11.3" stroke="var(--icon)" stroke-width="1.2"/></svg>
        000 000 0000
      </li>
      <li>
        <svg viewBox="0 0 14 14" aria-hidden="true"><rect x="0.5" y="2.5" width="13" height="9" fill="var(--icon)"/><polyline points="0.5,2.5 7,8 13.5,2.5" fill="none" stroke="#fff" stroke-width="1"/></svg>
        youremail@xyz.com
      </li>
      <li>
        <svg viewBox="0 0 14 14" aria-hidden="true"><g fill="none" stroke="var(--icon)" stroke-width="1"><circle cx="7" cy="7" r="6"/><ellipse cx="7" cy="7" rx="2.6" ry="6"/><line x1="1" y1="7" x2="13" y2="7"/><line x1="2" y1="4" x2="12" y2="4"/><line x1="2" y1="10" x2="12" y2="10"/></g></svg>
        www.velmarbuilds-ex.com
      </li>
    </ul>

    <address class="address">
      <span>0000, Anywhere, Somewhere<br>City, ST 0000</span>
      <svg viewBox="0 0 16 20" aria-hidden="true"><path d="M8 0.5a7 7 0 0 0-7 7c0 5 7 12 7 12s7-7 7-12a7 7 0 0 0-7-7z" fill="var(--icon)"/><circle cx="8" cy="7.5" r="2.6" fill="#fff"/></svg>
    </address>

    <div class="footer-band"></div>
  </section>

</body>
</html>
```